Plakate für Psychologische Beratung am Telefon
Zielgruppe
Psychologische Beratung am Telefon
Aufgabenstellung
anliegendes Word Dokument soll als eine Art 'Plakat' (pdf Datei) erstellt werden. Diese PDF Datei wird dann an alle MitarbeiterInnen gesandt und soll Auskunft über das Beratungsangebot geben. Die Farben bitte so wie auf dieser Website (das ist unser Mutterunternehmen). www.lindenhof-kolleg.com.

```html
<!DOCTYPE html>
<html lang="de">
<head>
<meta charset="utf-8">
<title>Psychologische Beratung am Telefon</title>
<link href="https://fonts.googleapis.com/css2?family=Fira+Sans+Extra+Condensed:wght@300;500&family=Open+Sans:wght@300;400&display=swap" rel="stylesheet">
<style>
:root{
  --bg:#a3a3a3;
  --paper:#ffffff;
  --brand-blue:#0a6a8f;
  --text-grey:#6b6b6b;
  --text-dark:#2b2b2b;
  --arrow-blue:#6aaed0;
  --logo-dark:#222222;
  --partner-brown:#8a7150;
}
*{margin:0;padding:0;box-sizing:border-box}
html,body{width:1200px;height:1200px;overflow:hidden;background:var(--bg)}
.poster{position:absolute;left:246px;top:91px;width:720px;height:1018px;background:var(--paper);overflow:hidden;font-family:"Open Sans",sans-serif;hyphens:auto;-webkit-hyphens:auto}
.hero{position:absolute;left:0;top:0;width:720px;height:491px;background:linear-gradient(135deg,#eef0f2 0%,#e3e4e6 35%,#d9cfcb 60%,#eceae7 100%)}
.brand{position:absolute;left:432px;top:56px;display:flex;align-items:center;gap:10px}
.brand-square{width:16px;height:16px;background:var(--logo-dark)}
.brand-name{font-weight:400;font-size:16px;letter-spacing:2px;color:var(--logo-dark);text-transform:uppercase}
.hero-claim{position:absolute;left:48px;width:300px;top:342px;text-align:center;font-family:"Fira Sans Extra Condensed",sans-serif;font-weight:300;font-size:18px;line-height:29px;color:var(--brand-blue);text-transform:uppercase}
.hero-claim strong{font-weight:500}
.col{position:absolute}
.col-left{left:43px;top:544px;width:310px}
.col-right{left:367px;top:534px;width:312px}
h2{font-family:"Fira Sans Extra Condensed",sans-serif;font-weight:500;font-size:19px;letter-spacing:1px;color:var(--brand-blue);text-transform:uppercase;margin-bottom:5px}
p,li{font-weight:300;font-size:13.8px;line-height:17.4px;color:var(--text-grey)}
.sub{font-weight:400;color:var(--brand-blue);margin-top:4px;hyphens:none}
.block{margin-bottom:19px}
.partner{display:flex;align-items:center;gap:8px;height:68px;margin-bottom:24px;padding-top:44px}
.partner-square{width:10px;height:10px;background:var(--partner-brown)}
.partner-name{font-weight:400;font-size:12px;color:var(--partner-brown);text-transform:uppercase;hyphens:none}
.dial{color:var(--text-dark);font-weight:400;hyphens:none}
.dial span{color:var(--brand-blue)}
.steps{list-style:none;margin-left:-6px}
.steps li{position:relative;padding-left:23px}
.steps svg{position:absolute;left:0;top:4px}
.hotline{position:absolute;left:367px;top:861px;width:309px;height:157px;background:var(--brand-blue);color:#fff;padding:10px 0 0 33px}
.hotline-number{font-weight:300;font-size:27px;letter-spacing:.5px;white-space:nowrap}
.hotline p{color:#fff;font-size:13px;line-height:19.5px;hyphens:none}
.hotline .times{margin-top:12px;font-size:14.5px;line-height:19.5px}
</style>
</head>
<body>
<div class="poster">
  <div class="hero" role="img" aria-label="Foto: Beraterin mit Headset am Schreibtisch in hellem Büro"></div>
  <div class="brand"><span class="brand-square"></span><span class="brand-name">Lindenhof Kolleg</span></div>
  <p class="hero-claim">Unsere <strong>Beraterinnen</strong> und <strong>Berater</strong> ver&shy;fügen alle über <strong>langjährige Beratungs&shy;erfahrung</strong> und je nach Thema auch über eine Psychotherapiezulassung.</p>

  <div class="col col-left">
    <div class="block">
      <h2>Für wen?</h2>
      <p>Für alle Mitarbeitenden und Führungskräfte der NH|FS</p>
    </div>
    <div class="block">
      <h2>Die Beratungsfelder</h2>
      <p class="sub">Private Anliegen:</p>
      <p>Partnerschaftskonflikte, Erziehungsberatung, Tren&shy;nung/Scheidung, Verlust, Trauer, Todesfall, Schock&shy;diagnosen usw.</p>
      <p class="sub">Psychische Gesundheit:</p>
      <p>Sucht und Abhängigkeiten, Depressionen, Burnout, Ängste usw.</p>
      <p class="sub">Berufliche Anliegen:</p>
      <p>Vereinbarkeit Beruf und Familie, Konflikte mit Kol&shy;leginnen oder Kollegen oder Vorgesetzten, Über&shy;forderungen am Arbeitsplatz sowie Coaching für Führungskräfte</p>
    </div>
  </div>

  <div class="col col-right">
    <div class="partner"><span class="partner-square"></span><span class="partner-name">Nordhafen Hochschule</span></div>
    <div class="block">
      <h2>Der Ablauf</h2>
      <p class="dial">Sie wählen <span>0451 555 20 190</span></p>
      <ul class="steps">
        <li><svg width="10" height="12" viewBox="0 0 10 12"><path d="M2 1l6 5-6 5" fill="none" stroke="var(--arrow-blue)" stroke-width="2"/></svg>Ihr Anruf wird von den psychologischen Assis&shy;tentinnen angenommen</li>
        <li><svg width="10" height="12" viewBox="0 0 10 12"><path d="M2 1l6 5-6 5" fill="none" stroke="var(--arrow-blue)" stroke-width="2"/></svg>Diese erfragen ein Stichwort zu Ihrem Anliegen, um Sie</li>
        <li><svg width="10" height="12" viewBox="0 0 10 12"><path d="M2 1l6 5-6 5" fill="none" stroke="var(--arrow-blue)" stroke-width="2"/></svg>direkt mit einer Expertin oder einem Experten für Ihr Thema verbinden zu können</li>
      </ul>
    </div>
    <div class="block">
      <h2>Anonymität</h2>
      <p>Die Beratung ist anonym. Sie müssen Ihren Namen nicht nennen.</p>
    </div>
  </div>

  <div class="hotline">
    <div class="hotline-number">0451 – 555 20 – 190</div>
    <p style="margin-top:8px">Sofortberatung oder Terminvereinbarung<br>zu Ihrer Wunschzeit</p>
    <p class="times">Di. 14:00 – 17:00 Uhr<br>Do.&nbsp; 9:00 – 12:00 Uhr</p>
  </div>
</div>
</body>
</html>
```